Exhibition Stand Design for innovative Social Business

We are an innovative social business empowering people to value nature through ZUN, a complementary digital currency. We have attached the TEK_ZUN branding document, and are needing a design for our exhibition stand (https://fairbuildlab.com/produit/stand-parapluie-classic-pvc-3x4c/. The attached doc mocks up a stand on page 32, though we would like some messaging included, in line with our website www.tekzun.ch. You will see there how the branding concept has been implemented with the TEK:GROW, SHARE, THRIVE wording, as well as Everyone wins. Our green colours are included in the branding document. Many thanks!

Industry/Entity Type

Environment

Font styles to use
Other font styles liked:
• As per our attached fonts

Requirements
Must have
• Our attached branding guidelines gives our look and feel - Innovative / Dynamic / Vibrant / Reliable / Accessible / Connected.

```html
<!DOCTYPE html>
<html lang="en">
<head>
<meta charset="utf-8">
<title>TEK ZUN exhibition stand</title>
<link rel="stylesheet" href="https://fonts.googleapis.com/css2?family=Montserrat:wght@600;700;800&family=Quicksand:wght@700&display=swap">
<style>
  :root {
    --page: #f2f2f2;
    --white: #ffffff;
    --ink: #111111;
    --green-left: #4de6ad;
    --green-right: #22f046;
    --glow: rgba(255, 255, 255, 0.32);
    --disc-light: #f4fff6;
    --disc-green: #6df08e;
  }
  html, body {
    margin: 0;
    width: 1200px;
    height: 1000px;
    overflow: hidden;
    background: var(--page);
  }
  .stand-banner {
    position: absolute;
    left: 100px;
    top: 120px;
    width: 1000px;
    height: 720px;
    overflow: hidden;
    background: linear-gradient(90deg, var(--green-left), var(--green-right));
    font-family: "Montserrat", Arial, sans-serif;
  }
  .header-band {
    position: absolute;
    left: 0; top: 0;
    width: 100%;
    height: 130px;
    background: var(--white);
    border-bottom: 5px solid var(--ink);
    display: flex;
    align-items: center;
    justify-content: center;
  }
  .brand-name {
    margin: 0;
    font-size: 96px;
    font-weight: 800;
    letter-spacing: 4px;
    color: var(--ink);
    line-height: 1;
  }
  .glow-circle {
    position: absolute;
    border-radius: 50%;
    background: var(--glow);
  }
  .glow-circle.top-right { width: 470px; height: 470px; left: 700px; top: 60px; }
  .glow-circle.bottom-left { width: 300px; height: 300px; left: -10px; top: 510px; }
  .pillar {
    position: absolute;
    top: 185px;
    width: 220px;
  }
  .pillar.grow { left: 80px; }
  .pillar.share { left: 390px; }
  .pillar.thrive { left: 695px; }
  .pillar-icon { display: block; width: 220px; height: 220px; }
  .pillar-label {
    margin: 12px 0 0 0;
    color: var(--white);
    line-height: 1;
  }
  .pillar.grow .pillar-label { margin-left: 62px; }
  .pillar.share .pillar-label { margin-left: 23px; }
  .pillar.thrive .pillar-label { margin-left: 17px; }
  .pillar-label .prefix {
    display: block;
    font-size: 20px;
    font-weight: 800;
    color: var(--ink);
  }
  .pillar-label .word {
    display: block;
    margin-top: 4px;
    font-size: 40px;
    font-weight: 700;
  }
  .tagline {
    position: absolute;
    left: 0; top: 528px;
    width: 100%;
    margin: 0;
    text-align: center;
    font-family: "Quicksand", Arial, sans-serif;
    font-weight: 700;
    font-size: 50px;
    color: var(--white);
  }
</style>
</head>
<body>
<main class="stand-banner">
  <div class="glow-circle top-right"></div>
  <div class="glow-circle bottom-left"></div>

  <header class="header-band">
    <h1 class="brand-name">TEK ZUN</h1>
  </header>

  <svg width="0" height="0" aria-hidden="true">
    <defs>
      <linearGradient id="disc-fill" x1="0" y1="1" x2="1" y2="0">
        <stop offset="0" stop-color="#f4fff6"/>
        <stop offset="1" stop-color="#6df08e"/>
      </linearGradient>
    </defs>
  </svg>

  <section class="pillar grow">
    <svg class="pillar-icon" viewBox="0 0 220 220" aria-hidden="true">
      <circle cx="110" cy="110" r="104" fill="var(--disc-green)" fill-opacity="0.5" stroke="var(--ink)" stroke-width="4"/>
      <circle cx="110" cy="110" r="88" fill="url(#disc-fill)"/>
      <path d="M110 170 L52 112 A30 30 0 0 1 110 70 A30 30 0 0 1 168 112 Z" fill="var(--ink)"/>
      <polyline points="82,112 104,112 112,94 122,132 130,104 136,112 180,112" fill="none" stroke="var(--white)" stroke-width="7" stroke-linejoin="round" stroke-linecap="round"/>
    </svg>
    <p class="pillar-label"><span class="prefix">TEK</span><span class="word">GROW</span></p>
  </section>

  <section class="pillar share">
    <svg class="pillar-icon" viewBox="0 0 220 220" aria-hidden="true">
      <circle cx="110" cy="110" r="104" fill="var(--disc-green)" fill-opacity="0.5" stroke="var(--ink)" stroke-width="4"/>
      <circle cx="110" cy="110" r="88" fill="url(#disc-fill)"/>
      <circle cx="110" cy="110" r="74" fill="var(--ink)"/>
      <circle cx="110" cy="110" r="60" fill="none" stroke="var(--white)" stroke-width="3"/>
      <text x="110" y="140" text-anchor="middle" font-family="Montserrat, Arial, sans-serif" font-weight="800" font-size="86" fill="var(--white)">$</text>
    </svg>
    <p class="pillar-label"><span class="prefix">TEK</span><span class="word">SHARE</span></p>
  </section>

  <section class="pillar thrive">
    <svg class="pillar-icon" viewBox="0 0 220 220">
      <circle cx="110" cy="110" r="104" fill="var(--disc-green)" fill-opacity="0.5" stroke="var(--ink)" stroke-width="4"/>
      <circle cx="110" cy="110" r="88" fill="url(#disc-fill)"/>
      <circle cx="110" cy="110" r="72" fill="var(--ink)" role="img" aria-label="Globe illustration"/>
    </svg>
    <p class="pillar-label"><span class="prefix">TEK</span><span class="word">THRIVE</span></p>
  </section>

  <p class="tagline">everyone wins</p>
</main>
</body>
</html>
```